Bright Pelvic Health Business Card

Need a business card for a surgical practice called Bright Pelvic Health. We have recently selected a logo (attached). The business card will need to have two formats:
1) One with the logo/physician name/ contact info on the front and location information on the back.
2) One in "appointment reminder card" style with the logo/ contact info/ date/ time on the front and the location information on the back.

The front side should include the following information:
- Logo
- Rohan K. Desai, MD FACOG
- phone: 469-555-0172
- fax: 1-469-555-0188
- email: admin@brightpelvic.example
- website: www.brightpelvichealth.example

The back side should have the office locations listed:
4815 Juniper Way, Plano, TX 75093
3720 Baywood Rd, Plano, TX 75025
2245 Larkspur Ln, Irving, TX 75038
815 W Finch St S310, Dallas, TX 75201
3516 Quarry Blvd, Grand Prairie, TX 75051
6437 Wexley Crest Dr, San Antonio, TX 78240
5822 Ember Rd, Pasadena, TX 77504

Target Market(s)

1. Other physicians who might refer patients
2. Female patients

Industry/Entity Type

Business

Font styles to use
Other font styles liked:
• Tahoma for lettering

Requirements
Must have
• As per the instructions
Should not have
• No other images needed -- please try to keep font consistent with logo design. Can use Tahoma as the font for lettering.

```html
<!DOCTYPE html>
<html lang="en">
<head>
<meta charset="utf-8">
<title>Bright Pelvic Health – Business Card</title>
<link rel="stylesheet" href="https://fonts.googleapis.com/css2?family=Open+Sans:wght@400;700&family=Didact+Gothic&display=swap">
<style>
  :root {
    --page-bg: #ffffff;
    --page-border: #dcdcdc;
    --card-bg: #f6f6f6;
    --card-border: #e3e3e3;
    --label: #9a9a9a;
    --brand-red: #e8343a;
    --brand-blue: #2a6ebb;
    --ink: #1f1f1f;
    --ink-soft: #3a3a3a;
  }
  * { margin: 0; padding: 0; box-sizing: border-box; }
  html, body { width: 1200px; height: 581px; overflow: hidden; background: var(--page-bg); }
  .sheet {
    position: relative; width: 1200px; height: 581px;
    border: 1px solid var(--page-border);
    font-family: "Open Sans", Tahoma, sans-serif;
  }
  .side-label {
    position: absolute; top: 62px;
    font-size: 16px; color: var(--label);
  }
  .side-label--front { left: 78px; }
  .side-label--back { left: 601px; }
  .card {
    position: absolute; top: 97px; width: 519px; height: 339px;
    background: var(--card-bg); border: 1px solid var(--card-border);
    overflow: hidden;
  }
  .card--front { left: 81px; }
  .card--back { left: 600px; border-left: none; }

  .brand {
    position: absolute; left: 30px; top: 170px;
    display: flex; align-items: center; gap: 7px; white-space: nowrap;
  }
  .brand__dot { width: 11px; height: 11px; border-radius: 50%; background: var(--brand-red); }
  .brand__name { font-size: 15px; font-weight: 700; color: var(--brand-blue); }

  .contact-rule {
    position: absolute; left: 236px; top: 154px;
    width: 3px; height: 82px; background: var(--brand-blue);
  }
  .person { position: absolute; left: 254px; top: 96px; white-space: nowrap; }
  .person__name { font-size: 20px; font-weight: 700; color: var(--brand-red); line-height: 1.2; }
  .person__name span { color: var(--ink); }
  .person__title { font-size: 12.5px; color: var(--ink); line-height: 1.2; }
  .contact-list {
    position: absolute; left: 256px; top: 148px;
    list-style: none; font-size: 14px; color: var(--ink); line-height: 1;
    white-space: nowrap; letter-spacing: -0.1px;
  }
  .contact-list li { display: flex; align-items: center; gap: 7px; height: 22px; }
  .contact-list li:nth-child(3) { margin-top: 4px; }
  .contact-list svg { width: 14px; height: 14px; flex: none; }

  .back-brand {
    position: absolute; left: 24px; top: 128px;
    font-size: 16px; font-weight: 700; color: var(--brand-blue); line-height: 1.25;
  }
  .locations {
    position: absolute; left: 183px; top: 40px;
    list-style: none; font-family: "Didact Gothic", Tahoma, sans-serif;
    font-size: 13.5px; color: var(--ink-soft); line-height: 25.3px; white-space: nowrap;
  }
</style>
</head>
<body>
<div class="sheet">
  <div class="side-label side-label--front">Front</div>
  <div class="side-label side-label--back">Back</div>

  <section class="card card--front">
    <div class="brand">
      <span class="brand__dot"></span>
      <span class="brand__name">Bright Pelvic Health</span>
    </div>

    <div class="person">
      <div class="person__name">Rohan K. Desai<span>,</span></div>
      <div class="person__title">MD FACOG</div>
    </div>
    <div class="contact-rule"></div>
    <ul class="contact-list">
      <li>
        <svg viewBox="0 0 16 16" fill="none" stroke="#333" stroke-width="1.3"><rect x="1.5" y="3.5" width="13" height="9"/><path d="M1.5 3.5 8 9l6.5-5.5"/></svg>
        admin@brightpelvic.example
      </li>
      <li>
        <svg viewBox="0 0 16 16" fill="none" stroke="#333" stroke-width="1.3"><circle cx="8" cy="8" r="6.5"/><ellipse cx="8" cy="8" rx="2.8" ry="6.5"/><path d="M1.5 8h13"/></svg>
        www.brightpelvichealth.example
      </li>
      <li>
        <svg viewBox="0 0 16 16" fill="none" stroke="#333" stroke-width="1.3"><rect x="4" y="1" width="8" height="14" rx="1.5"/><rect x="5.5" y="3" width="5" height="5" fill="#333" stroke="none"/><path d="M6 11h4M6 13h4"/></svg>
        469-555-0172
      </li>
      <li>
        <svg viewBox="0 0 16 16" fill="#333"><rect x="4" y="1.5" width="8" height="4"/><rect x="1" y="6" width="14" height="6" rx="1"/><rect x="4" y="11" width="8" height="3.5" fill="#fff" stroke="#333"/></svg>
        1-469-555-0188
      </li>
    </ul>
  </section>

  <section class="card card--back">
    <div class="back-brand">Bright<br>Pelvic<br>Health</div>
    <ul class="locations">
      <li>4815 Juniper Way, Plano, TX 75093</li>
      <li>3720 Baywood Rd, Plano, TX 75025</li>
      <li>2245 Larkspur Ln, Irving, TX 75038</li>
      <li>815 W Finch St S310, Dallas, TX 75201</li>
      <li>3516 Quarry Blvd, Grand Prairie, TX 75051</li>
      <li>6437 Wexley Crest Dr, San Antonio, TX 78240</li>
      <li>5822 Ember Rd, Pasadena, TX 77504</li>
    </ul>
  </section>
</div>
</body>
</html>
```